Educational Brochure or Pamphlet Series

We are a nonprofit organization looking at revamping our template designs for our educational pamphlet series, as we edit and republish our content library for 2014. Most of the current content spans over 3 to 4 panel double-sided folded brochures, although we are not limited to that format moving forward. We would be looking for a design that is inviting prompting interest at initial pick up, while also being laid out in a manner where complex tips and advice is able to be digested by readers. We do not have a consistent brand currently among our materials so we are able to branch to a new more modern and professional look/theme, but at the same time i wouldn't want to to go so far away from our look that we clash with our colors/logo/identity.

I almost chose magazine as project type, because ideally i would prefer a design that has the ability to grow beyond a 3 panel foldable brochure, into a small multipage booklet or magazine bound style.

We are a nonprofit in the health advocacy realm that helps patients understand the insurance and medical industry so they can get and afford the care they need while battling a major illness. We have not updated our publication design in over 10 years and need a professional refresh. More about us can be found at www.carewaybridge.org
Updates

Thanks to everyone that has already contributed designs or those who have accepted the project invite and are still working on submission.    I appreciate your willingness to assist our organization and participate in the process.   I look forward to reviewing the designs soon.

I am excited to participate in my first project on Pixel Harbor, and look forward to working again on future projects within this platform.

If you have any questions or could benefit from additional explanation on aspects of the project, please feel free to reach out to me and I'd be happy to share any insight I have.

Marna

Target Market(s)

Our pamphlets and brochures are geared towards patients who have been diagnosed with serious illness (ex. cancer, ALS, MS) and who are navigating the healthcare system to get the care and medications they need. Patients or caregivers would pick up these brochures in cancer facilities, doctors office or through online research.

Included in uploaded files are a few of these current pamphlets, some of our more recently designed ads or promo pieces to see what we have been doing lately. If needed and requested, i'd be happy to provide links of some of the brochures of our favorite partners who have done a nice job with presenting similar information.

Industry/Entity Type

Insurance

Font styles to use
Sans Serif

Colors

Designer to choose colors to be used in the design.

Requirements
Must have
• -Information easy to read and digest
-professional and educational in focus
-a design that can be reasonably customized or modified to include a number of corollary topics in a similar structure to complete a full library.
-colorful (can be 2 color or 4 color print)
-enough white space to be pleasing to the eye and not overwhelming with text
Nice to have
• could work on a lighthouse or beacon of light theme. (possible, ok if not)
Should not have
• ideally no extreme die cuts or printing specs that would be exceptionally expensive to produce, given nonprofit budget

```html
<!DOCTYPE html>
<html lang="en">
<head>
<meta charset="utf-8">
<title>Careway Bridge Foundation – Brochure Spread</title>
<link href="https://fonts.googleapis.com/css2?family=Arimo:wght@400;700&family=Alegreya:wght@400&family=PT+Sans:wght@700&display=swap" rel="stylesheet">
<style>
  :root {
    --backdrop: #d9d6d3;
    --paper: #e2dfdf;
    --ink: #2b2b2b;
    --accent: #2a86c5;
    --wave-deep: #1f74b4;
    --wave-mid: #3a9bd6;
    --wave-pale: #a9cde8;
    --white: #ffffff;
    --photo-a: #c9c4c0;
    --photo-b: #5b6470;
  }
  * { box-sizing: border-box; margin: 0; padding: 0; }
  html, body { width: 1200px; height: 970px; overflow: hidden; }
  body { background: var(--backdrop); position: relative; font-family: "Arimo", Arial, sans-serif; color: var(--ink); }

  .spread {
    position: absolute; left: 30px; top: 83px; width: 1140px; height: 805px;
    background: var(--paper); overflow: hidden;
  }
  .wave { position: absolute; left: 0; top: 0; width: 1140px; height: 805px; }

  .section-title {
    font-family: "Alegreya", Georgia, serif; font-weight: 400;
    color: var(--accent); font-size: 29px; line-height: 1;
  }
  .intro { position: absolute; left: 36px; top: 30px; width: 495px; }
  .intro p {
    font-size: 14.6px; line-height: 23.8px; margin: 4px 0 0 3px;
  }
  .intro .mission-title { margin-top: 5px; }
  .intro .assist-lead { margin-top: 4px; }
  .help-list { list-style: none; margin-top: 0; }
  .help-list li { color: var(--accent); font-size: 14.6px; line-height: 24px; }
  .help-list li:nth-child(1) { margin-left: 19px; }
  .help-list li:nth-child(2) { margin-left: 21px; }
  .help-list li:nth-child(3) { margin-left: 16px; }

  .services { position: absolute; left: 589px; top: 20px; width: 535px; }
  .service-list { list-style: none; margin-top: 4px; }
  .service-list li {
    font-size: 13.4px; line-height: 20px; text-align: justify;
    margin-left: 11px; margin-bottom: 12px;
  }
  .service-list li:nth-child(1) { margin-bottom: 14px; }
  .service-list li:nth-child(2) { margin-bottom: 10px; }
  .service-list li:nth-child(3) { margin-bottom: 15px; }
  .service-list li:nth-child(4) { margin-bottom: 12px; }
  .service-list li:nth-child(5) { margin-bottom: 11px; }
  .service-list li:nth-child(6),
  .service-list li:nth-child(7) { margin-bottom: 7px; }
  .service-list li:nth-child(8) { margin-bottom: 8px; }
  .service-list li:nth-child(9) { margin-bottom: 7px; }

  .team-photo {
    position: absolute; left: 105px; top: 362px; width: 466px; height: 326px;
    background: linear-gradient(180deg, var(--photo-a) 0%, var(--photo-b) 100%);
    clip-path: polygon(10px 100px, 40px 78px, 110px 58px, 180px 40px, 290px 8px, 330px 0, 370px 8px, 420px 90px, 466px 150px, 466px 326px, 0 326px, 0 130px);
  }

  .brand {
    position: absolute; left: 130px; top: 710px; width: 316px;
    color: var(--white);
  }
  .brand-name {
    display: flex; align-items: center; gap: 10px;
    font-family: "PT Sans", Arial, sans-serif; font-weight: 700; font-size: 30px; line-height: 0.98;
  }
  .brand-mark { width: 30px; height: 30px; background: var(--white); flex: none; }
  .brand-rule { height: 1px; background: var(--white); margin: 7px 0 4px; }
  .brand-tagline { font-family: "PT Sans", Arial, sans-serif; font-size: 9px; font-weight: 700; text-align: right; }

  .call {
    position: absolute; left: 710px; top: 742px;
    font-family: "PT Sans", Arial, sans-serif; font-weight: 700; font-size: 30px;
    color: var(--white);
  }
</style>
</head>
<body>
  <main class="spread">
    <svg class="wave" viewBox="0 0 1140 805" aria-hidden="true">
      <path d="M0 508 C 200 560, 420 690, 640 690 C 820 690, 980 620, 1140 590 L1140 805 L0 805 Z" fill="var(--wave-pale)"/>
      <path d="M0 545 C 200 610, 420 710, 620 700 C 800 690, 980 615, 1140 600 L1140 805 L0 805 Z" fill="var(--wave-mid)"/>
      <path d="M0 575 C 220 650, 430 700, 640 690 C 820 680, 980 625, 1140 610 L1140 805 L0 805 Z" fill="var(--wave-deep)" opacity="0.55"/>
    </svg>

    <section class="intro">
      <h2 class="section-title">About</h2>
      <p>Founded in 1996, CBF is a national non-profit, 501(c)3 direct patient services organization with a mission "to safeguard patients through effective mediation, assuring access to care, maintenance of employment &amp; preservation of financial stability."</p>
      <h2 class="section-title mission-title">Mission</h2>
      <p>Founded in 1996, CBF is a national non-profit, 501(c)3 direct patient services organization with a mission "to safeguard patients through effective mediation, assuring access to care, maintenance of employment &amp; preservation of financial stability."</p>
      <p class="assist-lead">We assist patients with:</p>
      <ul class="help-list">
        <li>Medical Debt Crisis</li>
        <li>Insurance Access Issues</li>
        <li>Job Retention Issues</li>
      </ul>
    </section>

    <section class="services">
      <h2 class="section-title">Services</h2>
      <ul class="service-list">
        <li>Navigate through the reimbursement system, including initial interpretation of the patient's benefit language</li>
        <li>Diligently negotiate insurance coverage for emerging drugs, durable medical equipment &amp; treatments</li>
        <li>Directly assist with coordination of benefit issues in the public &amp; private sectors</li>
        <li>Provide direct appeals assistance</li>
        <li>Provide educational resources, including disease-specific literature, managed care information &amp; financial resource information</li>
        <li>Provide referrals &amp; linkage to appropriate educational resources</li>
        <li>Provide clinical trials education &amp; conduct clinical trials screening</li>
        <li>Network patients to all known local, state and/or national resources for financial assistance.</li>
        <li>Provide case management services to uninsured patients, ensuring access to care &amp; enrollment into Medical and /or charity care programs, when appropriate</li>
        <li>Assist with preservation of employment</li>
      </ul>
    </section>

    <div class="team-photo" role="img" aria-label="Photo of four smiling professionals in business attire standing together"></div>

    <div class="brand">
      <div class="brand-name"><span class="brand-mark"></span><span>Careway Bridge<br>Foundation</span></div>
      <div class="brand-rule"></div>
      <div class="brand-tagline">Solving Insurance and Healthcare Access Problems | since 1996</div>
    </div>

    <div class="call">Call: (800)555-0142</div>
  </main>
</body>
</html>
```